Business card design needed

We need a business card design for our new company Velbrino Event Creations, based in Leeton NSW. We will however be serving the whole Riverina area. We plan any events like, Parties, Weddings ext. We would like to see designs that is vibrant but elegant. Mainly we would like to have our Name displayed on the front and all the other info at the back. We need a design that will catch the eye anywhere.Design FRONT AND BACK

Industry/Entity Type

Events

Contact Information for Business Card

Velbrino Event Creations
Tirsa Hallveck

0461539207
velbrino@quorvamail.com

Believe the Impossible

Requirements
Must have
• Elegant Coulors and Fonts

```html
<!DOCTYPE html>
<html lang="en">
<head>
<meta charset="utf-8">
<title>Velbrino Event Creations – Business Card</title>
<link rel="stylesheet" href="https://fonts.googleapis.com/css2?family=Josefin+Sans:wght@300;400;600&display=swap">
<style>
  :root {
    --backdrop: #8a8a8a;
    --card-black: #0b0b0b;
    --card-charcoal: #262626;
    --gold: #e2c27a;
    --gold-soft: #c9a65c;
    --ink-white: #f2f2f2;
    --ink-grey: #bdbdbd;
  }
  * { margin: 0; padding: 0; box-sizing: border-box; }
  html, body { width: 1200px; height: 861px; overflow: hidden; }
  body {
    background: var(--backdrop);
    font-family: "Josefin Sans", sans-serif;
    display: flex;
    align-items: center;
    justify-content: center;
    gap: 44px;
  }
  .card {
    position: relative;
    width: 520px;
    height: 297px;
    border-radius: 3px;
    overflow: hidden;
    background:
      linear-gradient(180deg, rgba(255,255,255,0.06) 0%, rgba(0,0,0,0) 45%, rgba(0,0,0,0.55) 100%),
      repeating-linear-gradient(90deg,
        rgba(255,255,255,0) 0px, rgba(255,255,255,0.05) 22px,
        rgba(255,255,255,0) 44px, rgba(255,255,255,0.025) 70px,
        rgba(255,255,255,0) 96px),
      radial-gradient(ellipse at 60% 0%, var(--card-charcoal) 0%, var(--card-black) 70%);
    box-shadow: 0 10px 28px rgba(0,0,0,0.35);
  }
  .card__content {
    position: absolute;
    inset: 0;
    display: flex;
    flex-direction: column;
  }

  /* Front */
  .card--front .card__content {
    align-items: center;
    justify-content: center;
  }
  .brand-name {
    color: var(--gold);
    font-weight: 600;
    letter-spacing: 0.06em;
    text-transform: uppercase;
    line-height: 1;
  }
  .card--front .brand-name { font-size: 44px; }
  .brand-line {
    color: var(--gold);
    font-weight: 600;
    font-size: 19px;
    letter-spacing: 0.28em;
    text-transform: uppercase;
    margin-top: 12px;
  }

  /* Back */
  .card--back .card__content {
    padding: 34px 34px 0 40px;
    align-items: flex-end;
  }
  .card--back .brand-name { font-size: 34px; text-align: right; }
  .card--back .brand-line { font-size: 14px; margin-top: 8px; }
  .dotted-rule {
    width: 300px;
    border-top: 2px dotted var(--gold-soft);
    margin: 16px 0 10px;
  }
  .person-name {
    color: var(--gold);
    font-weight: 400;
    font-size: 27px;
    letter-spacing: 0.12em;
    text-transform: uppercase;
    line-height: 1;
  }
  .dotted-rule--lower { margin: 10px 0 14px; }
  .contact-line {
    align-self: flex-start;
    color: var(--gold);
    font-weight: 300;
    font-size: 12.5px;
    letter-spacing: 0.04em;
  }
  .contact-line .label { text-transform: uppercase; }
  .tagline {
    align-self: flex-start;
    margin-top: 18px;
    color: var(--ink-grey);
    font-weight: 300;
    font-size: 18px;
    letter-spacing: 0.05em;
    text-transform: uppercase;
  }
  .tagline strong { color: var(--ink-white); font-weight: 400; }
</style>
</head>
<body>
  <section class="card card--front" aria-label="Business card front">
    <div class="card__content">
      <span class="brand-name">Velbrino</span>
      <span class="brand-line">Event Creations</span>
    </div>
  </section>

  <section class="card card--back" aria-label="Business card back">
    <div class="card__content">
      <span class="brand-name">Velbrino</span>
      <span class="brand-line">Event Creations</span>
      <div class="dotted-rule"></div>
      <span class="person-name">Tirsa Hallveck</span>
      <div class="dotted-rule dotted-rule--lower"></div>
      <p class="contact-line"><span class="label">Phone</span> 0461539207 | <span class="label">E-mail</span> velbrino@quorvamail.com</p>
      <p class="tagline"><strong>Believe</strong> the Impossible</p>
    </div>
  </section>
</body>
</html>
```